Entertainment Sound and Lighting company Business card

We need a professional looking business card designed for my growing entertainment sound and lighting company based in Sydney, Australia called "Kestrel Sound"

We provide technical production services (sound systems/lighting/vision) for events ranging from band gigs, weddings, corporate functions etc.

The business card needs to contain the following information:

Bartholomew Quenneville
Audio Engineer
Phone: 0478 615 027
Email: bartholomew@kestrelsound.com.au
Website: www.kestrelsound.com.au

Business logo has been attached in .ai format, please contact me if you need me to provide other files.

Target Market(s)

We need a business card that reflects our modern and professional company but still looks professional to appeal to our corporate clients.
We have a very broad target market spanning from bands needing PA systems for their gigs (18-30yrs) to event companies needing sound and lighting for weddings and other functions.

Industry/Entity Type

Business

Requirements
Must have
• Needs to include the logo that is attached of course, and the colour scheme.
Nice to have
• - Double sided

```html
<!DOCTYPE html>
<html lang="en">
<head>
<meta charset="utf-8">
<title>Kestrel Sound – Business Card</title>
<link href="https://fonts.googleapis.com/css2?family=Open+Sans:wght@700&family=Questrial&display=swap" rel="stylesheet">
<style>
  :root {
    --page: #ffffff;
    --page-edge: #c8c8c8;
    --card: #0b0c0e;
    --card-edge: #9a9a9a;
    --brand-blue: #02598b;
    --accent-blue: #0a5a8c;
    --brand-sky: #1a9ad6;
    --ink-light: #ffffff;
  }
  html, body {
    margin: 0;
    padding: 0;
    overflow: hidden;
    background: var(--page);
  }
  .canvas {
    position: relative;
    width: 1200px;
    height: 900px;
    box-sizing: border-box;
    border: 1px solid var(--page-edge);
    background: var(--page);
    overflow: hidden;
  }
  .card {
    position: absolute;
    background: var(--card);
    box-sizing: border-box;
    border: 1px solid var(--card-edge);
    overflow: hidden;
  }
  .card--front { left: 249px; top: 74px; width: 726px; height: 364px; }
  .card--back  { left: 250px; top: 455px; width: 726px; height: 364px; }

  .side-band {
    position: absolute;
    top: 34px;
    width: 9px;
    height: 296px;
    background: var(--accent-blue);
  }
  .side-band--left { left: 0; }
  .side-band--right { right: 0; }

  .brand-name {
    position: absolute;
    left: 0;
    right: 0;
    top: 212px;
    margin: 0;
    text-align: center;
    font-family: "Open Sans", Arial, sans-serif;
    font-weight: 700;
    font-size: 52px;
    line-height: 1;
    letter-spacing: -1px;
    color: var(--brand-sky);
  }
  .brand-mark {
    position: absolute;
    left: 355px;
    top: 140px;
    width: 16px;
    height: 16px;
    border-radius: 50%;
    background: var(--brand-sky);
  }
  .website {
    position: absolute;
    left: 0;
    right: 0;
    top: 273px;
    margin: 0;
    text-align: center;
    font-family: "Open Sans", Arial, sans-serif;
    font-weight: 700;
    font-size: 17px;
    color: var(--ink-light);
  }

  .identity {
    position: absolute;
    left: 20px;
    width: 312px;
    top: 158px;
    text-align: center;
    color: var(--ink-light);
  }
  .identity__name {
    margin: 0;
    font-family: "Open Sans", Arial, sans-serif;
    font-weight: 700;
    font-size: 20px;
    line-height: 1.2;
  }
  .identity__role {
    margin: 8px 0 0;
    font-family: "Questrial", "Century Gothic", sans-serif;
    font-size: 18px;
    line-height: 1.2;
  }

  .contact-panel {
    position: absolute;
    left: 378px;
    top: 35px;
    width: 348px;
    height: 294px;
    background: var(--brand-blue);
  }
  .contact-list {
    position: absolute;
    left: 22px;
    top: 125px;
    margin: 0;
    padding: 0;
    list-style: none;
    font-family: "Open Sans", Arial, sans-serif;
    font-weight: 700;
    font-size: 14px;
    line-height: 21px;
    color: var(--ink-light);
    white-space: nowrap;
  }
</style>
</head>
<body>
  <main class="canvas">
    <section class="card card--front" aria-label="Card front">
      <div class="side-band side-band--left"></div>
      <div class="side-band side-band--right"></div>
      <div class="brand-mark"></div>
      <h1 class="brand-name">Kestrel Sound</h1>
      <p class="website">www.kestrelsound.com.au</p>
    </section>

    <section class="card card--back" aria-label="Card back">
      <div class="identity">
        <p class="identity__name">Bartholomew Quenneville</p>
        <p class="identity__role">Audio Engineer</p>
      </div>
      <div class="contact-panel">
        <ul class="contact-list">
          <li>Phone: 0478 615 027</li>
          <li>Email: bartholomew@kestrelsound.com.au</li>
        </ul>
      </div>
    </section>
  </main>
</body>
</html>
```